Brindle Property Management email template

Looking for an email template for communications sent to residents that reads well in most email formats including mobile devices. Similar to the attached email, not quite reclaimed wood but something warm with interesting texture

```html
<!DOCTYPE html>
<html lang="en">
<head>
<meta charset="utf-8">
<title>Brindle Property Management – Resident Email</title>
<link href="https://fonts.googleapis.com/css2?family=Crimson+Text:wght@600;700&family=Montserrat:wght@400;500;600&family=Poppins:wght@300;400&display=swap" rel="stylesheet">
<style>
  :root{
    --espresso:#3a271c;
    --rust:#a4562c;
    --tan:#e0b98c;
    --sand:#f4e9da;
    --cream:#fffaf3;
    --body-text:#4d4037;
    --white:#ffffff;
    --wash-deep:#c88a55;
    --wash-light:#ecd3b4;
    --hero-1:#d9b48c;
    --hero-2:#a8774f;
    --hero-3:#6f4b32;
  }
  *{box-sizing:border-box;margin:0;padding:0}
  html,body{width:1200px;height:2798px;overflow:hidden;background:var(--cream)}
  body{position:relative;font-family:"Poppins",Arial,sans-serif;color:var(--body-text)}

  .preheader{position:absolute;top:0;left:0;width:1200px;height:75px;background:var(--sand);
    display:flex;align-items:center;justify-content:center;
    font-family:Arial,Helvetica,sans-serif;font-size:21px;color:var(--espresso)}

  .backdrop{position:absolute;top:75px;left:0;width:1200px;height:1200px;
    background:
      linear-gradient(180deg,rgba(255,250,243,0) 0%,rgba(255,250,243,0) 55%,var(--cream) 100%),
      repeating-linear-gradient(100deg,rgba(90,55,30,.07) 0 2px,rgba(255,255,255,0) 2px 9px,rgba(90,55,30,.04) 9px 10px,rgba(255,255,255,0) 10px 17px),
      linear-gradient(90deg,var(--wash-deep) 0%,var(--wash-light) 12%,var(--wash-light) 88%,var(--wash-deep) 100%)}

  .email{position:absolute;top:75px;left:150px;width:900px;height:2178px;background:var(--white);
    box-shadow:0 0 12px rgba(60,35,20,.22)}

  .brand{height:313px;display:flex;flex-direction:column;align-items:center;justify-content:center}
  .brand-name{font-family:"Montserrat",sans-serif;font-weight:600;font-size:40px;color:var(--espresso);
    letter-spacing:1px;text-align:center;line-height:1.25}

  .main-nav{height:90px;background:var(--espresso);display:flex;align-items:center;justify-content:center;gap:42px;
    font-family:"Montserrat",sans-serif;font-weight:500;font-size:25px}
  .main-nav a{color:var(--tan);text-decoration:none}
  .main-nav a.is-current{color:var(--white)}

  .hero{position:relative;height:575px;
    background:radial-gradient(ellipse at 35% 40%,var(--hero-1) 0%,var(--hero-2) 60%,var(--hero-3) 100%)}
  .hero-notch{position:absolute;left:400px;bottom:-1px}

  .content{text-align:center;padding-top:52px}
  .headline{font-family:"Crimson Text",serif;font-weight:700;font-size:56px;color:var(--espresso);line-height:1.1}
  .slogan{font-family:Arial,Helvetica,sans-serif;font-size:25px;color:#4a382c;margin-top:14px}
  .intro{width:830px;margin:38px auto 0;font-size:21px;line-height:30px;font-weight:400}
  .intro p+p{margin-top:30px}

  .section-title{display:inline-block;margin-top:90px;font-family:"Crimson Text",serif;font-weight:600;
    font-size:38px;color:var(--rust);padding-bottom:6px;border-bottom:4px solid var(--rust)}

  .feature-list{list-style:none;text-align:left;margin:79px 0 0 168px}
  .feature-list li{display:flex;align-items:center;height:54px;font-size:21px}
  .feature-list li::before{content:"";width:15px;height:15px;background:var(--rust);margin-right:30px}

  .cta{display:flex;align-items:center;justify-content:center;width:613px;height:77px;margin:92px auto 0;
    background:var(--rust);color:var(--white);text-decoration:none;
    font-family:"Montserrat",sans-serif;font-weight:600;font-size:31px;letter-spacing:5px}

  .site-footer{position:absolute;top:2253px;left:0;width:1200px;height:361px;background:var(--espresso);
    color:var(--white);text-align:center;font-family:"Montserrat",sans-serif}
  .footer-brand{display:flex;align-items:center;justify-content:center;gap:22px;margin-top:76px;
    font-weight:600;font-size:27px}
  .footer-brand::before{content:"";width:34px;height:34px;background:var(--white)}
  .contact-line{margin-top:82px;font-size:22px}
  .contact-line strong{font-weight:600}
  .contact-line .sep{margin:0 22px}
  .address{margin-top:26px;font-size:22px}

  .social{position:absolute;top:2660px;left:0;width:1200px;display:flex;justify-content:center;gap:8px}
  .social a{width:74px;height:74px;border-radius:50%;display:flex;align-items:center;justify-content:center;
    font-family:"Montserrat",sans-serif;font-size:14px;font-weight:600;color:var(--white);text-decoration:none}
  .social .s1{background:#8a5a3a}
  .social .s2{background:#c8925e}
  .social .s3{background:#a4402c}
</style>
</head>
<body>
  <div class="preheader">Don't see this email properly? View in web browser</div>
  <div class="backdrop" role="img" aria-label="Warm textured watercolour wash background"></div>

  <main class="email">
    <header class="brand">
      <div class="brand-name">Brindle<br>Property Management</div>
    </header>

    <nav class="main-nav">
      <a href="#" class="is-current">HOME</a>
      <a href="#">ABOUT</a>
      <a href="#">SERVICES</a>
      <a href="#">CONTACT</a>
    </nav>

    <div class="hero" role="img" aria-label="Photo of a large shingled house with a white wraparound porch and a lawn">
      <svg class="hero-notch" width="100" height="51" viewBox="0 0 100 51" aria-hidden="true">
        <polygon points="0,51 50,0 100,51" fill="#ffffff"/>
      </svg>
    </div>

    <section class="content">
      <h1 class="headline">Lorel Ipsum Dolor Sit Amet</h1>
      <p class="slogan">sub heading/slogan goes her</p>
      <div class="intro">
        <p>Nam eget justo porttitor, dictum eros quis, lobortis lacus. Donec malesuada libero sit amet ultricies vestibulum. Nulla sed risus id elit tempus tempus ac et nibh. Curabitur dolor risus, hendrerit vitae nunc eu, fringilla porta orci. Pellentesque congue eu sem eget venenatis.</p>
        <p>Nullam sem diam, dignissim non faucibus molestie, placerat eget nisi. Etiam eget ultricies nisi. Donec bibendum enim in ex blandit pulvinar. Nulla cursus eu nunc sed tempus. Sed placerat sodales metus quis venenatis. Aenean et velit vitae leo facilisis tristique.</p>
      </div>

      <h2 class="section-title">Sub Heading</h2>
      <ul class="feature-list">
        <li>In viverra ipsum a lectus convallis porttitor.</li>
        <li>Donec id diam et quam commodo tristique.</li>
        <li>Aliquam porta nisi a porttitor porta.</li>
        <li>Etiam id nisi sagittis lorem facilisis condimentum.</li>
      </ul>

      <a class="cta" href="#">CALL TO ACTION</a>
    </section>
  </main>

  <footer class="site-footer">
    <div class="footer-brand">BRINDLE PROPERTY MANAGEMENT</div>
    <p class="contact-line"><strong>Phone:</strong> 555 .0142.7788<span class="sep">|</span><strong>Email:</strong> info@brindlepropertymanagement.com</p>
    <p class="address">Harrow Lane 24, 4410 KB Fairmont, USA</p>
  </footer>

  <div class="social">
    <a href="#" class="s1">Share</a>
    <a href="#" class="s2">Follow</a>
    <a href="#" class="s3">Watch</a>
  </div>
</body>
</html>
```